Super Greens Label for Supplement Bottle

We want to design a front label for a health supplement bottle. The product is called Meadow Twist Chews™. This will be a new product so there is no current website for the product. The focus is on supergreens that taste great and deliver support for energy, digestion, and immune defense.
We want it to be modern, vibrant and appealing.
Bottle size: standard size supplement CLEAR bottle size, with white child resistant cap and the label panel dimensions are 3” x 7”. The label should be primarily white and green, with a touch of red; (see color palettes)/it can also ONLY be white and green. See samples attached.
We are only focused on the front of the bottle design, not on the back, but leave space for the supplement panel and other text on the back.
So the text for the front of the bottle is:
RT Balden's
Meadow Twist Chews™
Super Greens Blend for:
Energy, Digestion, and Immune Support*
60 Gummies | Dietary Supplement
Raspberry Flavor Gummies
Off to side of the label:
Non-GMO
Vegan Friendly
Plant-Based
Gelatin Free
Colors
Designer to choose colors to be used in the design.

```html
<!DOCTYPE html>
<html lang="en">
<head>
<meta charset="utf-8">
<title>Meadow Twist Chews – Front Label</title>
<link href="https://fonts.googleapis.com/css2?family=Fira+Sans:wght@400;500;600;700;800&display=swap" rel="stylesheet">
<style>
  :root {
    --bg-top: #f8b9a0;
    --bg-bottom: #fde3cf;
    --green-deep: #1c6b36;
    --green: #2f8a45;
    --green-light: #7dbb57;
    --red: #e8354c;
    --red-deep: #c8233a;
    --white: #ffffff;
    --ink-green: #1f5e33;
    --produce-a: #6e9a4a;
    --produce-b: #c9d9b0;
    --berry: #d93a4f;
  }
  * { box-sizing: border-box; margin: 0; padding: 0; }
  html, body { width: 1200px; height: 1200px; overflow: hidden; }
  body {
    background: linear-gradient(180deg, var(--bg-top) 0%, var(--bg-bottom) 100%);
    font-family: "Fira Sans", Arial, sans-serif;
    position: relative;
  }
  .label {
    position: absolute;
    left: 220px; top: 180px;
    width: 760px; height: 840px;
    background: var(--white);
    overflow: hidden;
    box-shadow: 0 10px 40px rgba(120, 60, 40, 0.18);
  }
  .label-bands { position: absolute; inset: 0; width: 100%; height: 100%; }
  .brand-pill {
    position: absolute; left: 50%; top: 118px;
    transform: translateX(-50%);
    background: var(--red);
    border: 3px solid var(--white);
    border-radius: 40px;
    padding: 6px 34px;
    color: var(--white);
    font-weight: 500; font-size: 40px; line-height: 1.1;
    white-space: nowrap;
  }
  .product-name {
    position: absolute; left: 0; right: 0; top: 200px;
    text-align: center;
    color: var(--white);
    font-weight: 600; font-size: 84px; line-height: 90px;
  }
  .product-name sup { font-size: 32px; vertical-align: top; line-height: 1; }
  .benefits {
    position: absolute; left: 0; right: 0; top: 398px;
    text-align: center; color: var(--white);
    font-weight: 600; font-size: 24px; line-height: 28px;
  }
  .produce-photo {
    position: absolute; left: 215px; top: 535px;
    width: 330px; height: 190px;
    border-radius: 18px;
    background: radial-gradient(ellipse at 50% 40%, var(--produce-b) 0%, var(--produce-a) 60%, var(--green-deep) 100%);
  }
  .claim-badge {
    position: absolute; width: 112px; height: 112px;
    border: 4px solid var(--green);
    border-radius: 50%;
    background: var(--white);
    display: flex; flex-direction: column; align-items: center; justify-content: center;
    gap: 2px;
    color: var(--green-deep);
    text-align: center;
  }
  .claim-badge svg { width: 34px; height: 34px; }
  .claim-badge .claim-text {
    font-weight: 700; font-size: 12.5px; line-height: 13px;
    letter-spacing: 0.3px; text-transform: uppercase;
  }
  .claim-badge.left-top { left: 50px; top: 535px; }
  .claim-badge.left-bottom { left: 50px; top: 662px; }
  .claim-badge.right-top { right: 50px; top: 535px; }
  .claim-badge.right-bottom { right: 50px; top: 662px; }
  .flavor {
    position: absolute; left: 0; right: 0; top: 736px;
    display: flex; justify-content: center; align-items: center; gap: 14px;
  }
  .berry-art {
    width: 60px; height: 42px; border-radius: 21px;
    background: radial-gradient(circle at 40% 40%, #f26b7c, var(--berry) 70%);
  }
  .flavor-text { color: var(--red-deep); text-align: left; line-height: 1; }
  .flavor-text .flavor-main { font-weight: 800; font-size: 32px; letter-spacing: 1px; }
  .flavor-text .flavor-sub { font-weight: 600; font-size: 12px; letter-spacing: 1px; margin-top: 2px; }
  .net-count {
    position: absolute; left: 0; right: 0; top: 796px;
    text-align: center; color: var(--ink-green);
    font-weight: 500; font-size: 24px; line-height: 28px;
  }
</style>
</head>
<body>
  <main class="label">
    <svg class="label-bands" viewBox="0 0 760 840" preserveAspectRatio="none" aria-hidden="true">
      <rect x="0" y="0" width="760" height="520" fill="var(--green-deep)"/>
      <path d="M0 175 C 200 120, 420 80, 760 95 L760 470 C 560 430, 300 520, 0 470 Z" fill="var(--red)"/>
      <path d="M0 470 C 300 520, 560 430, 760 470 L760 520 C 560 480, 300 560, 0 520 Z" fill="var(--green)"/>
      <path d="M0 500 C 300 550, 560 460, 760 500 L760 840 L0 840 Z" fill="var(--white)"/>
      <path d="M0 510 C 300 560, 560 470, 760 510" fill="none" stroke="var(--green-light)" stroke-width="4"/>
    </svg>

    <div class="brand-pill">RT Balden's</div>
    <h1 class="product-name">Meadow Twist<br>Chews<sup>™</sup></h1>
    <p class="benefits">Super Greens Blend for:<br>Energy, Digestion, and Immune Support*</p>

    <div class="claim-badge left-top">
      <svg viewBox="0 0 48 48" aria-hidden="true"><path d="M10 38 C10 18, 24 8, 40 8 C40 26, 30 38, 10 38 Z M10 38 L28 20" fill="none" stroke="var(--green)" stroke-width="4" stroke-linecap="round"/></svg>
      <span class="claim-text">Non-GMO</span>
    </div>
    <div class="claim-badge left-bottom">
      <svg viewBox="0 0 48 48" aria-hidden="true"><path d="M24 42 V22 M24 22 C24 12, 14 8, 8 10 C8 18, 16 24, 24 22 M24 26 C24 16, 34 12, 40 14 C40 22, 32 28, 24 26" fill="none" stroke="var(--green)" stroke-width="4" stroke-linecap="round"/></svg>
      <span class="claim-text">Plant-<br>Based</span>
    </div>
    <div class="claim-badge right-top">
      <svg viewBox="0 0 48 48" aria-hidden="true"><path d="M10 25 L20 35 L38 13" fill="none" stroke="var(--green)" stroke-width="5" stroke-linecap="round" stroke-linejoin="round"/></svg>
      <span class="claim-text">Vegan<br>Friendly</span>
    </div>
    <div class="claim-badge right-bottom">
      <svg viewBox="0 0 48 48" aria-hidden="true"><circle cx="24" cy="24" r="16" fill="none" stroke="var(--green)" stroke-width="4"/><path d="M13 35 L35 13" stroke="var(--green)" stroke-width="4" stroke-linecap="round"/></svg>
      <span class="claim-text">Gelatin<br>Free</span>
    </div>

    <div class="produce-photo" role="img" aria-label="Photo of fresh leafy greens, broccoli and cabbage in a woven basket"></div>

    <div class="flavor">
      <div class="berry-art" role="img" aria-label="Illustration of ripe raspberries with a leaf"></div>
      <div class="flavor-text">
        <div class="flavor-main">RASPBERRY</div>
        <div class="flavor-sub">FLAVOR GUMMIES</div>
      </div>
    </div>

    <p class="net-count">60 Gummies | Dietary Supplement</p>
  </main>
</body>
</html>
```